Book Cover Design: Backgammon - Ultra Brainy Brainy Test

Book cover design for a self-published book to be sold on Brindlo as a paperback as well as ebook.
The reader takes a quiz of 100 backgammon positions and then see how they fared versus 12 of the best players in the world. The pros then give explanations as to why they made their plays.

Th designs I had are a bit flat so far.

The special thing about this book is 12 of best in world taking the quiz before the reader. That is the attraction…

So how about design where photos of all 12 of them are showing within a backgammon board. You can leave the space for their pics and I insert later or you do once won contract.

But focus on the geniuses would be great, thank you!

Target Market(s)

Backgammon game enthusiasts

Requirements
Must have
• Picture of a backgammon board and idea quiz and top players in the world involved. Author’s name Oren Paskett
Nice to have
• Idea that 12 world class expert backgammon players all contributed to the book

```html
<!DOCTYPE html>
<html lang="en">
<head>
<meta charset="utf-8">
<title>Backgammon – Ultra Brainy Brainy Test</title>
<link href="https://fonts.googleapis.com/css2?family=Montserrat:wght@800&family=PT+Sans+Narrow:wght@400;700&display=swap" rel="stylesheet">
<style>
  :root {
    --page: #ffffff;
    --cover: #6f2d0e;
    --cover-deep: #64270b;
    --accent: #c5865a;
    --text-light: #ffffff;
    --wood-light: #c98a52;
    --wood-mid: #a8632f;
    --wood-dark: #7a3a15;
  }
  * { margin: 0; padding: 0; box-sizing: border-box; }
  html, body {
    width: 1002px;
    height: 1200px;
    overflow: hidden;
    background: var(--page);
  }
  .book-cover {
    position: absolute;
    left: 111px;
    top: 50px;
    width: 780px;
    height: 1100px;
    background: radial-gradient(ellipse at 50% 70%, var(--cover) 0%, var(--cover-deep) 100%);
    overflow: hidden;
  }
  .board-photo {
    position: absolute;
    left: 0;
    top: 0;
    width: 780px;
    height: 506px;
    background: linear-gradient(160deg, var(--wood-dark) 0%, var(--wood-mid) 35%, var(--wood-light) 60%, var(--wood-mid) 85%, var(--cover) 100%);
    clip-path: polygon(0 0, 100% 0, 100% 60%, 50% 100%, 0 60%);
  }
  .centered {
    position: absolute;
    left: 0;
    width: 100%;
    text-align: center;
  }
  .author {
    top: 552px;
    font-family: "Montserrat", sans-serif;
    font-weight: 800;
    font-size: 43px;
    color: var(--text-light);
    line-height: 1;
  }
  .ornament-dot {
    position: absolute;
    left: 381px;
    width: 18px;
    height: 18px;
    border-radius: 50%;
    border: 2px solid var(--accent);
    background: radial-gradient(circle, var(--accent) 0 4px, transparent 5px);
  }
  .dot-top { top: 637px; }
  .dot-bottom { top: 1006px; }
  .title {
    top: 680px;
    font-family: "Montserrat", sans-serif;
    font-weight: 800;
    font-size: 74px;
    letter-spacing: 0.5px;
    color: var(--text-light);
    line-height: 1;
  }
  .subtitle {
    top: 753px;
    font-family: "PT Sans Narrow", sans-serif;
    font-weight: 700;
    font-size: 36px;
    letter-spacing: 7px;
    color: var(--accent);
    line-height: 1;
  }
  .divider {
    position: absolute;
    left: 238px;
    top: 823px;
    width: 304px;
    height: 20px;
  }
  .count {
    top: 877px;
    font-family: "Montserrat", sans-serif;
    font-weight: 800;
    font-size: 32px;
    color: var(--text-light);
    line-height: 1;
  }
  .tagline {
    top: 921px;
    font-family: "PT Sans Narrow", sans-serif;
    font-weight: 700;
    font-size: 20px;
    color: var(--accent);
    line-height: 22px;
  }
</style>
</head>
<body>
  <main class="book-cover">
    <div class="board-photo" role="img" aria-label="Photo of a wooden backgammon board corner with light and dark checkers and two dice"></div>

    <p class="centered author">Oren Paskett</p>
    <span class="ornament-dot dot-top"></span>

    <h1 class="centered title">BACKGAMMON</h1>
    <p class="centered subtitle">Ultra Brainy Brainy Test</p>

    <svg class="divider" viewBox="0 0 304 20" aria-hidden="true">
      <polygon points="0,10 110,7 110,13" fill="#c5865a"/>
      <polygon points="304,10 194,7 194,13" fill="#c5865a"/>
      <circle cx="152" cy="10" r="8" fill="none" stroke="#c5865a" stroke-width="2"/>
      <circle cx="152" cy="10" r="4" fill="#c5865a"/>
    </svg>

    <h2 class="centered count">100 POSITIONS</h2>
    <p class="centered tagline">Pit your wits against the geniuses,<br>then get an insight into their thinking</p>

    <span class="ornament-dot dot-bottom"></span>
  </main>
</body>
</html>
```